Images for my Portfolio

Hi,

I will use this theme

http://themes.corvanelli-studio.com/html/nimbra/light/index.html#work

and need 1 nice big image for each of my projects. So we have 9 images at the end but for mockup 1 image is enough for me to get an idea. The images should show different aspects of the site, so for example:

https://www.hopfenglanz.de/

There we have:
- Slideshow
- Configurator
- Cart etc.

Just have a look around and see whats special. Feel free in image-size and styling-elemets: frames, polaroid, 2D, 3D, mobile devices - do whatever you would do if you were me: a web-designer who wants to explain his last projects to the visitors.

Projects are:

https://www.hopfenglanz.de
http://taldorwinkel.de/
http://movirex.de
http://www.bistro-bruehgeraete-welt.de/
http://www.veltrapress.de/blog/info/klebefolien/
http://km-sprachmittlerin.de/de/
http://trn-appraisal.de/
http://zutrittsring-markt7.de/
http://www.blank-und-flink.de/

This is not advertisement for my clients. I sell websites (!) so the purpose of the images is that my visitor can see what is possible if he hires me.

Thanks a lot

```html
<!DOCTYPE html>
<html lang="de">
<head>
<meta charset="utf-8">
<title>Malzfreude – Startseite</title>
<link rel="stylesheet" href="https://fonts.googleapis.com/css2?family=Source+Sans+3:wght@300;400;600;700&display=swap">
<style>
  :root {
    --header-bg: #1f1f1f;
    --hero-bg: #3b3b3b;
    --hero-bg-dark: #2e2e2e;
    --accent: #e6ad17;
    --text-light: #e9e9e9;
    --text-muted: #9a9a9a;
    --page-bg: #f4f4f4;
    --text-dark: #3a3a3a;
    --button-dark: #262626;
    --rule: #d6d6d6;
  }
  * { box-sizing: border-box; margin: 0; padding: 0; }
  html, body { width: 1200px; height: 750px; overflow: hidden; }
  body {
    font-family: "Source Sans 3", "Helvetica Neue", Arial, sans-serif;
    background: var(--page-bg);
    color: var(--text-dark);
  }
  .site { width: 1200px; height: 750px; position: relative; overflow: hidden; }

  /* Header */
  .site-header {
    height: 120px;
    background: var(--header-bg);
    position: relative;
  }
  .brand {
    position: absolute; left: 90px; top: 36px;
    display: flex; align-items: center; gap: 12px;
    color: var(--accent); font-size: 30px; font-weight: 400; line-height: 1;
  }
  .brand-dot { width: 26px; height: 26px; border-radius: 50%; background: var(--accent); }
  .service-bar {
    position: absolute; right: 90px; top: 14px;
    display: flex; align-items: center; gap: 6px;
  }
  .service-note { color: var(--text-muted); font-size: 11px; letter-spacing: .5px; margin-right: 14px; }
  .service-note strong { color: var(--accent); font-weight: 600; }
  .service-btn {
    background: var(--accent); color: var(--header-bg);
    font-size: 10px; font-weight: 700; letter-spacing: .6px;
    padding: 6px 12px;
  }
  .main-nav {
    position: absolute; right: 90px; top: 58px;
    display: flex; gap: 34px; list-style: none;
  }
  .main-nav li {
    color: var(--text-light); font-size: 13px; font-weight: 600;
    text-transform: uppercase; text-align: center; line-height: 1.15;
  }

  /* Hero slideshow */
  .hero {
    height: 340px;
    background: linear-gradient(180deg, var(--hero-bg) 0%, var(--hero-bg-dark) 100%);
    position: relative;
  }
  .hero-copy { position: absolute; left: 230px; top: 82px; width: 380px; text-align: center; }
  .hero-title { color: var(--text-light); font-size: 32px; font-weight: 300; line-height: 1.2; }
  .hero-lead { color: var(--accent); font-size: 20px; line-height: 1.3; margin-top: 8px; }
  .hero-actions { display: flex; gap: 12px; justify-content: center; margin-top: 22px; }
  .hero-btn {
    background: var(--button-dark); color: var(--text-light);
    font-size: 14px; padding: 8px 18px; border: 1px solid #4a4a4a;
  }
  .hero-visual {
    position: absolute; left: 660px; top: 40px;
    width: 330px; height: 300px;
    background: radial-gradient(ellipse at 40% 50%, #4a4a4a 0%, #222 70%);
    border-radius: 4px 4px 0 0;
  }
  .slide-arrow { position: absolute; top: 150px; }
  .slide-arrow.prev { left: 130px; }
  .slide-arrow.next { right: 130px; }

  /* Intro section */
  .intro { text-align: center; padding-top: 46px; }
  .intro-title { font-size: 30px; font-weight: 400; color: var(--text-dark); line-height: 1.2; }
  .intro-title em { font-style: normal; color: var(--accent); }
  .intro-sub {
    margin: 18px auto 0; width: 640px;
    font-size: 15px; color: var(--text-muted);
    display: flex; align-items: center; gap: 14px;
  }
  .intro-sub::before, .intro-sub::after { content: ""; flex: 1; height: 1px; background: var(--rule); }
  .intro-sub a { color: var(--accent); text-decoration: none; }
  .steps { display: flex; justify-content: center; gap: 56px; margin-top: 30px; }
  .step-icon {
    width: 86px; height: 86px; border-radius: 50%;
    border: 4px solid #e2e2e2;
  }
  .step-icon.beer { background: radial-gradient(circle, #e6ad17 0%, #9b6e0d 100%); }
  .step-icon.hops { background: radial-gradient(circle, #a9c85a 0%, #5d7a26 100%); }
  .step-icon.gauge { background: radial-gradient(circle, #ffffff 0%, #cfcfcf 100%); }
  .step-icon.foam { background: radial-gradient(circle, #f6cf5a 0%, #d39a12 100%); }
  .step-icon.glass { background: radial-gradient(circle, #f2c23c 0%, #c88e0e 100%); }
</style>
</head>
<body>
<div class="site">
  <header class="site-header">
    <div class="brand"><span class="brand-dot"></span>Malzfreude</div>
    <div class="service-bar">
      <span class="service-note">LIEFERUNG <strong>INNERHALB WENIGER TAGE</strong></span>
      <span class="service-btn">KONTO</span>
      <span class="service-btn">HILFE</span>
      <span class="service-btn">LOGIN</span>
      <span class="service-btn">WARENKORB</span>
    </div>
    <ul class="main-nav">
      <li>Bier<br>konfigurieren</li>
      <li>Unsere<br>Besten &amp; Mehr</li>
      <li>Als<br>Geschenk</li>
      <li>Für<br>Events</li>
      <li><br>Fragen</li>
    </ul>
  </header>

  <section class="hero">
    <svg class="slide-arrow prev" width="16" height="26" viewBox="0 0 16 26"><polyline points="13,2 3,13 13,24" fill="none" stroke="#e9e9e9" stroke-width="3"/></svg>
    <div class="hero-copy">
      <h1 class="hero-title">Als exklusives Biergeschenk.</h1>
      <p class="hero-lead">Individuelles Bier schenken.<br>Origineller geht es nicht.</p>
      <div class="hero-actions">
        <span class="hero-btn">Mehr erfahren</span>
        <span class="hero-btn">Jetzt schenken ›</span>
      </div>
    </div>
    <div class="hero-visual" role="img" aria-label="Produktfoto: Bierflasche, gefülltes Glas und Geschenkbox mit roter Schleife"></div>
    <svg class="slide-arrow next" width="16" height="26" viewBox="0 0 16 26"><polyline points="3,2 13,13 3,24" fill="none" stroke="#e9e9e9" stroke-width="3"/></svg>
  </section>

  <section class="intro">
    <h2 class="intro-title">Für den besonderen Moment das besondere Bier. <em>Deins.</em></h2>
    <p class="intro-sub"><span>Bier selbst konfigurieren: so geht's <a href="#">(zum Film)</a></span></p>
    <div class="steps">
      <div class="step-icon beer" role="img" aria-label="Foto: Bierglas"></div>
      <div class="step-icon hops" role="img" aria-label="Foto: Hopfendolden"></div>
      <div class="step-icon gauge" role="img" aria-label="Foto: Anzeige für Bitterkeit"></div>
      <div class="step-icon foam" role="img" aria-label="Foto: Bierschaum"></div>
      <div class="step-icon glass" role="img" aria-label="Foto: helles Bier"></div>
    </div>
  </section>
</div>
</body>
</html>
```